Flat Belly Design Graphics for Social

I want to create 9 social media graphics (new Instagram size 4:5 (1080 x 1350 pixels) focusing on our Flat Belly Graphics, using the pics attached. Use the attached pics, NO RANDOM STOCK PHOTOGRAPHY. For the color scheme of the graphics, the color palette is attached. YOU MUST POST ALL 9 GRAPHICS IN ONE ENTRY.
Using the 3 titles below, create one set of graphics. 1) with all text, then for the others, use the pictures as detailed below in IMPORTANT:
1. 21-Night Lean Middle Reboot Beyond 50
2. The 20-Second Trim-Core Menu Guide
3. Starlet Tricks to a Slender Midline Beyond 50 - Zero Scalpel Needed
IMPORTANT:
Only use RK Pic 1 and RK Pic 2 with the title, 21-Night Lean Middle Reboot Beyond 50
Only use meal plan1 and meal plan2 pics with the title, 20-Second Trim-Core Menu Guide
Only use starlet tricks 1 and starlet tricks 2 pics with the title, Starlet Tricks to a Slender Midline Beyond 50 - Zero Scalpel Needed
women over 40

```html
<!DOCTYPE html>
<html lang="en">
<head>
<meta charset="utf-8">
<title>Lean Middle Graphics Set</title>
<link rel="stylesheet" href="https://fonts.googleapis.com/css2?family=Dancing+Script:wght@600;700&family=Montserrat:wght@800;900&family=Nunito:wght@300;400;600;800&display=swap">
<style>
  :root {
    --page: #ffffff;
    --blush: #f6dce1;
    --blush-light: #fbeef0;
    --rose: #ebb5c4;
    --rose-line: #e09fb2;
    --ink: #2e4e4a;
    --photo-skin: #c79a86;
    --photo-table: #6b4a36;
    --photo-light: #e9d6cf;
  }
  * { box-sizing: border-box; margin: 0; padding: 0; }
  html, body { width: 1200px; height: 849px; overflow: hidden; background: var(--page); }
  .sheet { position: relative; width: 1200px; height: 849px; }

  .card {
    position: absolute; width: 272px; height: 340px; overflow: hidden;
    background: radial-gradient(ellipse at 55% 40%, var(--blush-light) 0%, var(--blush) 70%);
    color: var(--ink); font-family: "Nunito", sans-serif;
  }
  .col-1 { left: 103px; } .col-2 { left: 464px; } .col-3 { left: 825px; }
  .row-1 { top: 52px; } .row-2 { top: 456px; }

  .frame { position: absolute; inset: 14px; border: 1px solid var(--rose-line); z-index: 3; pointer-events: none; }
  .arch {
    position: absolute; left: 0; right: 0; bottom: 0; height: 78px;
    background: linear-gradient(180deg, var(--rose) 0%, #f1c6d2 100%);
    border-radius: 60px 60px 0 0; z-index: 1;
  }
  .row-2 .arch { height: 85px; }

  .line { position: absolute; left: 0; right: 0; text-align: center; line-height: 1; z-index: 4; white-space: nowrap; }
  .kicker { font-weight: 300; font-size: 17px; letter-spacing: .5px; }
  .headline { font-family: "Montserrat", sans-serif; font-weight: 900; letter-spacing: .3px; }
  .script { font-family: "Dancing Script", cursive; font-weight: 700; }
  .teaser { font-size: 13px; line-height: 1.15; }
  .teaser .light { font-weight: 300; }
  .teaser .strong { font-weight: 800; font-size: 15px; }
  .byline { font-family: "Dancing Script", cursive; font-weight: 700; font-size: 19px; }
  .credential { font-size: 7px; font-weight: 600; }
  .row-2 .byline { font-size: 27px; }
  .row-2 .credential { font-size: 11px; font-weight: 600; }

  .photo { position: absolute; z-index: 2; }
  .swoosh { position: absolute; z-index: 4; }
  .swoosh path { fill: none; stroke: var(--ink); stroke-width: 2.5; stroke-linecap: round; }
</style>
</head>
<body>
<main class="sheet">

  <!-- Reboot title, photo version -->
  <section class="card row-1 col-1">
    <div class="arch"></div>
    <p class="line kicker" style="top:24px">21-Night Lean</p>
    <p class="line headline" style="top:44px;font-size:24px">MIDDLE REBOOT</p>
    <p class="line script" style="top:72px;left:auto;right:36px;font-size:26px">Beyond 50</p>
    <svg class="swoosh" style="left:140px;top:104px" width="92" height="12"><path d="M2 10 Q40 2 90 3"/></svg>
    <div class="line teaser" style="top:132px;left:auto;right:26px;text-align:right">
      <span class="light">The Hidden reasons</span><br>
      <span class="strong">you can’t lose</span><br>
      <span class="strong">the belly fat</span>
    </div>
    <div class="photo" role="img" aria-label="Smiling author in a white cropped sweater pointing to her flat stomach"
         style="left:0;top:115px;width:112px;height:225px;border-radius:50px 50px 0 0;background:linear-gradient(180deg,var(--photo-skin) 0%,#efe9e6 45%,#2b2b2b 100%)"></div>
    <p class="line byline" style="top:296px;left:130px;right:8px">By RK Sterling</p>
    <p class="line credential" style="top:320px;left:130px;right:8px">#1 Metro Ledger Bestselling Author</p>
  </section>

  <!-- Menu guide title, photo version -->
  <section class="card row-1 col-2">
    <div class="arch"></div>
    <p class="line kicker" style="top:24px">The 20-Second</p>
    <p class="line headline" style="top:44px;font-size:27px">TRIM-CORE</p>
    <p class="line headline" style="top:72px;font-size:27px">MENU GUIDE</p>
    <div class="photo" role="img" aria-label="Healthy foods around a printed meal plan sheet on a wooden table"
         style="left:0;top:107px;width:272px;height:182px;border-radius:34px;background:radial-gradient(circle at 50% 55%,#f4f2ef 0 22%,var(--photo-table) 40%,#8a5c40 100%)"></div>
    <p class="line byline" style="top:300px">By RK Sterling</p>
    <p class="line credential" style="top:324px">#1 Metro Ledger Bestselling Author</p>
  </section>

  <!-- Starlet tricks title, photo version -->
  <section class="card row-1 col-3">
    <div class="arch"></div>
    <p class="line kicker" style="top:24px">Starlet Tricks to</p>
    <p class="line headline" style="top:44px;font-size:21px">A SLENDER MIDLINE</p>
    <p class="line headline" style="top:68px;font-size:34px">BEYOND 50</p>
    <p class="line script" style="top:120px;left:8px;right:auto;width:110px;font-size:36px">Zero</p>
    <p class="line script" style="top:158px;left:8px;right:auto;width:110px;font-size:22px">Scalpel</p>
    <p class="line script" style="top:184px;left:8px;right:auto;width:110px;font-size:22px">Needed</p>
    <svg class="swoosh" style="left:20px;top:208px" width="92" height="14"><path d="M2 12 Q40 3 90 2"/></svg>
    <div class="photo" role="img" aria-label="Two fit women, one whispering a secret to the other who looks excited"
         style="left:120px;top:128px;width:152px;height:212px;border-radius:50px 50px 0 0;background:linear-gradient(180deg,#5a3a2c 0%,var(--photo-skin) 30%,#f0d6d4 60%,#5d7aa3 100%)"></div>
    <p class="line byline" style="top:282px;left:0;right:auto;width:116px">By RK Sterling</p>
    <p class="line credential" style="top:306px;left:0;right:auto;width:116px;line-height:1.3">#1 Metro Ledger<br>Bestselling Author</p>
  </section>

  <!-- Reboot title, text version -->
  <section class="card row-2 col-1">
    <div class="arch"></div>
    <div class="frame"></div>
    <p class="line kicker" style="top:28px">21-Night Lean</p>
    <p class="line headline" style="top:50px;font-size:30px">MIDDLE</p>
    <p class="line headline" style="top:82px;font-size:46px">REBOOT</p>
    <p class="line script" style="top:136px;font-size:30px">Beyond 50</p>
    <svg class="swoosh" style="left:86px;top:172px" width="100" height="12"><path d="M2 10 Q45 2 98 3"/></svg>
    <div class="line teaser" style="top:192px;font-size:14px">
      <span class="light">The Hidden reasons</span><br>
      <span class="strong">you can’t lose</span><br>
      <span class="strong">the belly fat</span>
    </div>
    <p class="line byline" style="top:268px">By RK Sterling</p>
    <p class="line credential" style="top:306px"># 1 Metro Ledger Bestselling Author</p>
  </section>

  <!-- Menu guide title, text version -->
  <section class="card row-2 col-2">
    <div class="arch"></div>
    <div class="frame"></div>
    <p class="line kicker" style="top:52px">The 20-Second</p>
    <p class="line headline" style="top:74px;font-size:30px">TRIM-CORE</p>
    <p class="line headline" style="top:110px;font-size:52px">MENU</p>
    <p class="line headline" style="top:164px;font-size:52px">GUIDE</p>
    <p class="line byline" style="top:268px">By RK Sterling</p>
    <p class="line credential" style="top:306px"># 1 Metro Ledger Bestselling Author</p>
  </section>

  <!-- Starlet tricks title, text version -->
  <section class="card row-2 col-3">
    <div class="arch"></div>
    <div class="frame"></div>
    <p class="line kicker" style="top:28px">Starlet Tricks to</p>
    <p class="line headline" style="top:50px;font-size:21px">A SLENDER MIDLINE</p>
    <p class="line headline" style="top:78px;left:30px;right:auto;font-size:100px;letter-spacing:-2px">50</p>
    <p class="line headline" style="top:84px;left:196px;right:auto;width:30px;height:100px;font-size:24px;writing-mode:vertical-rl;transform:rotate(180deg)">BEYOND</p>
    <p class="line script" style="top:196px;font-size:21px">– Zero Scalpel Needed</p>
    <svg class="swoosh" style="left:150px;top:222px" width="90" height="12"><path d="M2 10 Q40 2 88 3"/></svg>
    <p class="line byline" style="top:268px">By RK Sterling</p>
    <p class="line credential" style="top:306px"># 1 Metro Ledger Bestselling Author</p>
  </section>

</main>
</body>
</html>
```